Business card design needed

A mobile coffee, eats and treats van. We sell freshly ground Morlandi coffee, a selection of yummy things to eats, and lovely giftwares, including candles, scarfs, jewellery. We also have an online store where additional home and giftwares can be purchased
Updates

Thanks so much for all your efforts so far, I have received some great concepts.  Just wanted to send out a reminder that our concept is coffee, eats and treats (the treats being home and gift ware)  We have a mobile van and also an online store.  I dont want to make my business card too "busy" but at the same time I would like to give my potential customers something that will really excite and intrigue them...

Thank you everyone for your designs...I think I have made a decision...have just sent out a couple of questions.  I will be loading a new project shortly if you are interested?  Thanks, Helena

Industry/Entity Type

Store

Contact Information for Business Card

The Little Sparrow - Coffee, Eats & Treats
Helena Marquardt
0439 582 616
helena@thelittlesparrow.com.au
www.thelittlesparrow.com.au
www.facebook.com/thelittlesparrow
https://twitter.com/TheLittleSparrow

Requirements
Nice to have
• It would be good to have a rewards program on the back, we can tick off when prople buy coffee....5th coffee free...something like that...

It would also be good for the card to look like a gift tag....

```html
<!DOCTYPE html>
<html lang="en">
<head>
<meta charset="utf-8">
<title>The Little Sparrow – Business Card &amp; Rewards Tag</title>
<link rel="stylesheet" href="https://fonts.googleapis.com/css2?family=Josefin+Sans:wght@300;400;600;700&display=swap">
<style>
  :root{
    --backdrop:#2e2e2f;
    --card:#f1efe3;
    --gold:#b3a36b;
    --ink:#3a3424;
    --text:#2f2b22;
    --icon:#8c8a82;
    --dash:#3a3a3a;
    --eyelet:#9a9a9a;
  }
  *{margin:0;padding:0;box-sizing:border-box}
  html,body{width:1200px;height:1000px;overflow:hidden;background:var(--backdrop)}
  body{position:relative;font-family:"Josefin Sans",sans-serif;color:var(--text)}

  .card{position:absolute;background:var(--card);overflow:hidden}
  .card--front{left:280px;top:113px;width:628px;height:355px}
  .card--back{left:280px;top:521px;width:630px;height:357px}

  .eyelet{position:absolute;width:14px;height:14px;border-radius:50%;
    background:var(--backdrop);border:3px solid var(--eyelet)}
  .card--front .eyelet{left:11px;top:178px}
  .card--back .eyelet{right:15px;top:178px}

  .brand{position:absolute;display:flex;flex-direction:column;align-items:flex-end}
  .brand__name{font-weight:700;color:var(--gold);letter-spacing:-0.3px;line-height:1;white-space:nowrap}
  .brand__tagline{font-weight:600;color:var(--ink);letter-spacing:1px;margin-top:6px;white-space:nowrap}

  .card--front .brand{left:28px;top:76px;width:258px}
  .card--front .brand__name{font-size:28px}
  .card--front .brand__tagline{font-size:9px}

  .contact__person{position:absolute;left:34px;top:188px;font-size:25px;font-weight:300;color:var(--text)}
  .contact__list{position:absolute;left:46px;top:226px;list-style:none}
  .contact__item{display:flex;align-items:center;height:20px;font-size:11.5px;font-weight:300;color:var(--text)}
  .contact__icon{width:18px;height:14px;margin-right:14px;flex:none}

  .photo{position:absolute;right:0;top:0;width:330px;height:355px}

  .card--back .brand{left:0;right:0;top:70px;align-items:center}
  .card--back .brand__name{font-size:48px}

  .rewards__offer{position:absolute;left:0;right:0;top:178px;text-align:center;
    font-size:22px;font-weight:400;letter-spacing:0.4px;color:var(--text)}
  .rewards__stamps{position:absolute;left:70px;top:216px;display:flex;gap:21px}
  .rewards__stamp{width:107px;height:105px;border:2px dashed var(--dash)}
</style>
</head>
<body>

<section class="card card--front">
  <span class="eyelet"></span>
  <div class="brand">
    <span class="brand__name">The Little Sparrow</span>
    <span class="brand__tagline">COFFEE, EATS &amp; TREATS</span>
  </div>

  <p class="contact__person">Helena Marquardt</p>
  <ul class="contact__list">
    <li class="contact__item">
      <svg class="contact__icon" viewBox="0 0 18 14"><path d="M2 5c0-3 14-3 14 0l-3 1-1-2H6L5 6zM4 7h10l1 6H3z" fill="var(--icon)"/></svg>
      0439 582 616
    </li>
    <li class="contact__item">
      <svg class="contact__icon" viewBox="0 0 18 14"><rect x="1" y="2" width="16" height="10" fill="var(--icon)"/><path d="M1 2l8 6 8-6" stroke="var(--card)" stroke-width="1.4" fill="none"/></svg>
      helena@thelittlesparrow.com.au
    </li>
    <li class="contact__item">
      <svg class="contact__icon" viewBox="0 0 18 14"><g fill="none" stroke="var(--icon)" stroke-width="1.2"><circle cx="9" cy="7" r="6"/><ellipse cx="9" cy="7" rx="2.6" ry="6"/><path d="M3 7h12"/></g></svg>
      www.thelittlesparrow.com.au
    </li>
    <li class="contact__item">
      <svg class="contact__icon" viewBox="0 0 18 14"><circle cx="9" cy="7" r="5" fill="var(--icon)"/></svg>
      www.facebook.com/thelittlesparrow
    </li>
    <li class="contact__item">
      <svg class="contact__icon" viewBox="0 0 18 14"><circle cx="9" cy="7" r="5" fill="var(--icon)"/></svg>
      https://twitter.com/TheLittleSparrow
    </li>
  </ul>

  <svg class="photo" viewBox="0 0 330 355" role="img" aria-label="Photo of a cup of black coffee on a saucer surrounded by roasted coffee beans on a wooden table">
    <defs>
      <radialGradient id="coffeeTones" cx="0.55" cy="0.45" r="0.7">
        <stop offset="0" stop-color="#8a5a36"/>
        <stop offset="0.6" stop-color="#5c3a22"/>
        <stop offset="1" stop-color="#3a2415"/>
      </radialGradient>
    </defs>
    <path d="M18 0H330V355H8C34 300 30 240 16 190C4 140 6 60 18 0Z" fill="var(--card)"/>
    <path d="M26 0H330V355H18C44 300 40 240 26 190C14 140 16 60 26 0Z" fill="#ffffff"/>
    <path d="M32 0H330V355H26C52 300 48 240 34 190C22 140 22 60 32 0Z" fill="url(#coffeeTones)"/>
  </svg>
</section>

<section class="card card--back">
  <span class="eyelet"></span>
  <div class="brand">
    <span class="brand__name">The Little Sparrow</span>
  </div>
  <p class="rewards__offer">BUY COFFEE AND GET 5TH COFFEE FREE</p>
  <div class="rewards__stamps">
    <span class="rewards__stamp"></span>
    <span class="rewards__stamp"></span>
    <span class="rewards__stamp"></span>
    <span class="rewards__stamp"></span>
  </div>
</section>

</body>
</html>
```